Book cover for modern/pop-culture-oriented poetry collection

We need a simple, streamlined book-cover design (that'll ultimately be 1600 x 2500 pixels; 300 dpi) for a book of poems. We would like to see three elements on the cover: (1) the title in all caps (GLASSHOURS); (2) the author name in all caps (MIRA TOLLEN); (3) the main image (attached, slugged "glasshours image"). Image and text should be centered on the cover.

Target Market(s)

Readers of contemporary poetry

Font styles to use
Sans Serif

Requirements
Must have
• Book title, author name, attached photo
Nice to have
• Also attached is the cover of a book (HARBOUR) that is in the style/spirit of what we're looking for.

```html
<!DOCTYPE html>
<html lang="en">
<head>
<meta charset="utf-8">
<title>Glasshours — Mira Tollen</title>
<link href="https://fonts.googleapis.com/css2?family=Josefin+Sans:wght@300&display=swap" rel="stylesheet">
<style>
  :root {
    --page: #ffffff;
    --cover: #141a1d;
    --ink: #ffffff;
    --glow-teal: #7fc4cc;
    --glow-orange: #8a3a1e;
  }
  html, body {
    margin: 0;
    width: 1200px;
    height: 1200px;
    overflow: hidden;
    background: var(--page);
  }
  .book-cover {
    position: absolute;
    left: 300px;
    top: 100px;
    width: 600px;
    height: 1000px;
    background: var(--cover);
    overflow: hidden;
  }
  .cover-photo {
    position: absolute;
    left: 0;
    top: 300px;
    width: 600px;
    height: 520px;
    background:
      radial-gradient(ellipse 90px 110px at 292px 236px, var(--glow-teal) 0%, rgba(127,196,204,0.55) 55%, rgba(127,196,204,0) 100%),
      radial-gradient(ellipse 230px 180px at 280px 230px, var(--glow-orange) 0%, rgba(138,58,30,0.5) 55%, rgba(20,26,29,0) 100%),
      var(--cover);
  }
  .cover-title,
  .cover-author {
    position: absolute;
    left: 0;
    width: 600px;
    margin: 0;
    text-align: center;
    color: var(--ink);
    font-family: "Josefin Sans", sans-serif;
    font-weight: 300;
    line-height: 1;
  }
  .cover-title {
    top: 122px;
    font-size: 48px;
    letter-spacing: 0.52em;
    text-indent: 0.52em;
  }
  .cover-author {
    top: 888px;
    font-size: 41px;
    letter-spacing: 0.72em;
    text-indent: 0.72em;
  }
</style>
</head>
<body>
  <main class="book-cover">
    <h1 class="cover-title">GLASSHOURS</h1>
    <div class="cover-photo" role="img" aria-label="glasshours image: a vintage orange television glowing with a teal screen in a dark room"></div>
    <p class="cover-author">MIRA TOLLEN</p>
  </main>
</body>
</html>
```